Marcus Lindqvist Photography needs a business card designs

I am looking for a business card with a logo clean and simple which I can use that logo on my website or on my pictures. It has to be very classy and very professional. Please look at my website at www.marcuslvqphoto.com for my signature. I'm thinking of something like that for my signature/logo. I'm still working on my website but you get an idea. I'm open to any design but not too busy graphics.

I will be printing the business card from qrivel.com.

Surprise me :)

contact me if you have any questions.

-ML

I'm receiving a lot of black background at the moment. I know my website is all black doesn't mean I want my card to be all black. Please send in with some white background as well. Thanks :)

check out some business cards that I found online. I think they are simple and look really awesome. I don't want a card that is too busy.

http://www.marcuslvqphoto.com/p270092084

Reason: Please extend the date for me. I haven't really receive any good design yet.

Printing

• -a logo that related to my first and last initial of my name "ML"
-double sided
• -I don't want my background to be all black.
-no pictures on the card

```html
<!DOCTYPE html>
<html lang="en">
<head>
<meta charset="utf-8">
<title>Marcus Lindqvist Photography – Business Card</title>
<link rel="stylesheet" href="https://fonts.googleapis.com/css2?family=Raleway:wght@400;500;700;800&display=swap">
<style>
  :root {
    --backdrop: #2b2628;
    --card-white: #ffffff;
    --card-white-shade: #eef2f3;
    --teal: #5b8e9b;
    --teal-dark: #3d6a77;
    --teal-light: #8fb6c0;
    --teal-text: #6a9aa6;
    --logo-disc: #e4eef0;
    --rule: #9dbec6;
  }
  * { box-sizing: border-box; margin: 0; padding: 0; }
  html, body {
    width: 1200px; height: 871px; overflow: hidden;
    background: var(--backdrop);
    font-family: "Raleway", sans-serif;
  }
  .canvas {
    width: 1200px; height: 871px;
    display: flex; align-items: center; justify-content: center; gap: 40px;
  }
  .card {
    position: relative;
    width: 540px; height: 309px;
    border-radius: 20px;
    overflow: hidden;
    box-shadow: 0 14px 30px rgba(0,0,0,.45);
  }

  /* Back side */
  .card-back {
    background: linear-gradient(135deg, var(--teal) 0%, var(--teal-dark) 100%);
  }
  .card-back .diagonal {
    position: absolute; inset: 0;
  }
  .card-back .mark-disc {
    position: absolute; left: 50%; top: 50%;
    width: 150px; height: 150px; margin: -75px 0 0 -75px;
    border-radius: 50%;
    background: var(--logo-disc);
    display: flex; align-items: center; justify-content: center;
    font-weight: 700; font-size: 58px; color: var(--teal); letter-spacing: 1px;
  }

  /* Front side */
  .card-front {
    background: linear-gradient(160deg, var(--card-white) 0%, var(--card-white-shade) 100%);
    color: var(--teal-text);
  }
  .card-front .diagonal { position: absolute; inset: 0; }
  .logo-disc {
    position: absolute; left: 24px; top: 24px;
    width: 66px; height: 66px; border-radius: 50%;
    background: var(--teal-light);
    display: flex; align-items: center; justify-content: center;
    font-weight: 700; font-size: 26px; color: var(--card-white);
  }
  .identity { position: absolute; left: 104px; top: 36px; }
  .identity .name {
    font-weight: 800; font-size: 31px; color: var(--teal-text); line-height: 1;
  }
  .identity .role {
    text-align: right; font-weight: 500; font-size: 13px; margin-top: 1px;
  }
  .website {
    position: absolute; left: 30px; top: 178px; font-size: 13px;
  }
  .contact-rule {
    position: absolute; left: 22px; right: 0; top: 200px;
    height: 1px; background: var(--rule);
  }
  .contact-list {
    position: absolute; left: 30px; top: 212px; list-style: none; font-size: 13px;
  }
  .contact-list li, .social-list li {
    display: flex; align-items: center; gap: 8px; height: 22px;
  }
  .contact-list svg { width: 12px; height: 12px; }
  .social-list {
    position: absolute; left: 330px; top: 244px; list-style: none; font-size: 15px;
  }
  .social-square {
    width: 13px; height: 13px; border-radius: 2px; background: var(--teal-text);
  }
</style>
</head>
<body>
<main class="canvas">

  <section class="card card-back" aria-label="Card back">
    <svg class="diagonal" viewBox="0 0 540 309" preserveAspectRatio="none" aria-hidden="true">
      <line x1="150" y1="309" x2="430" y2="0" stroke="#ffffff" stroke-opacity=".25" stroke-width="1"/>
    </svg>
    <div class="mark-disc">ML</div>
  </section>

  <section class="card card-front" aria-label="Card front">
    <svg class="diagonal" viewBox="0 0 540 309" preserveAspectRatio="none" aria-hidden="true">
      <line x1="0" y1="150" x2="120" y2="0" stroke="#9dbec6" stroke-opacity=".45" stroke-width="1"/>
    </svg>
    <div class="logo-disc">ML</div>
    <div class="identity">
      <div class="name">Marcus Lindqvist</div>
      <div class="role">photographer</div>
    </div>
    <div class="website">www.marcuslvqphoto.com</div>
    <div class="contact-rule"></div>
    <ul class="contact-list">
      <li>
        <svg viewBox="0 0 12 12" aria-hidden="true">
          <circle cx="6" cy="6" r="5.3" fill="none" stroke="#6a9aa6" stroke-width="1"/>
          <path d="M4.3 3.4c-.6.4-.6 1.4.2 2.6.8 1.3 1.9 2.3 2.7 2.1l.6-.8-1-.8-.6.4c-.5-.3-1-.9-1.3-1.5l.4-.6-.7-1.1z" fill="#6a9aa6"/>
        </svg>
        +1 903 555 01 42
      </li>
      <li>
        <svg viewBox="0 0 12 12" aria-hidden="true">
          <rect x=".8" y="2.5" width="10.4" height="7" fill="none" stroke="#6a9aa6" stroke-width="1"/>
          <path d="M.8 2.5L6 6.5l5.2-4" fill="none" stroke="#6a9aa6" stroke-width="1"/>
        </svg>
        marcusl@lvqmail.com
      </li>
    </ul>
    <ul class="social-list">
      <li><span class="social-square"></span>marcus.lindqvist</li>
      <li><span class="social-square"></span>@marcuslvqphoto</li>
    </ul>
  </section>

</main>
</body>
</html>
```